Create a Graphic About YOURSELF and PixelHarbor

PixelHarbor would like you (designers) to create an awesome graphic to promote YOURSELF and your profile on PixelHarbor!

Your graphic should communicate your name, your services and should mention PixelHarbor.

The design should be perfect for sharing on Chatterly. Here's an example of what we'd like http://blog.pixelharbor-example.ca/article/333/pixelharbor-launches-3000-hire-me-social-design-contest

Once you submitted your design, we'd love you to share the design ('advertisement') and promote yourself and PixelHarbor to your friends and potential customers. So make your submissions great and get your friends to vote for your design by 'Liking' it on Chatterly!

Prizes:
$1500 - "PixelHarbor Community" prize awarded to the designer with the most Chatterly 'Likes'
5 x $50 for the next 5 'most liked' designs on Chatterly

$1000 - "Hire Me" prize awarded to the designer who receives the most client invites
5 x $50 for the next 5 'most invited' designers

In summary, this is a great opportunity for you to increase your exposure to PixelHarbor customers and win cash prizes. Show off your design skills and get hired by PixelHarbor customers from around the world!

Target Market(s)

Fans, friends and customers of YOU

Industry/Entity Type

Cash

Requirements
Must have
• 1) Include your PixelHarbor user name on the graphic so customers can find you in the PixelHarbor Designer Directory
2) Include the tagline "Hire Me on PixelHarbor.com!" in your graphic design.
3) Share your design's URL on our Chatterly wall at http://chatterly-example.com/pixelharbor and get your friends to 'like' your design.
Nice to have
• 1) Include a tagline that expresses your design approach/philosophy
2) Artwork dimensions: 403 x 403 px
3) You can submit more than 1 design!
Should not have
• You must own the copyright of any images you use including stock imagery.

```html
<!DOCTYPE html>
<html lang="en">
<head>
<meta charset="utf-8">
<title>Hire Me – Prism Lane Media on PixelHarbor</title>
<link rel="stylesheet" href="https://fonts.googleapis.com/css2?family=Anton&family=Gochi+Hand&display=swap">
<style>
  :root {
    --parchment-light: #d9bf95;
    --parchment-mid: #c6a57a;
    --parchment-dark: #9c7b55;
    --crack: #8a5a2c;
    --chalk: #fbf7ef;
    --panel-black: #0b0b0b;
    --stripe-grey: #3a3a3a;
    --paper-white: #f7f1e8;
    --peach-splash: #e9b98f;
    --brand-pink: #f04fa0;
    --media-grey: #d5d5d5;
    --harbor-blue: #1f4e9c;
  }
  * { margin: 0; padding: 0; box-sizing: border-box; }
  html, body { width: 1200px; height: 901px; overflow: hidden; background: var(--parchment-mid); }
  .canvas {
    position: relative;
    width: 1200px;
    height: 901px;
    overflow: hidden;
    background:
      radial-gradient(ellipse 55% 45% at 30% 40%, var(--parchment-light), transparent 70%),
      radial-gradient(ellipse 40% 35% at 88% 80%, var(--peach-splash), transparent 70%),
      linear-gradient(160deg, var(--parchment-light) 0%, var(--parchment-mid) 55%, var(--parchment-dark) 100%);
  }
  .artwork { position: absolute; inset: 0; }
  .headline {
    position: absolute;
    left: 425px;
    top: 56px;
    font-family: "Anton", sans-serif;
    font-size: 78px;
    letter-spacing: 4px;
    color: var(--chalk);
    line-height: 1;
  }
  .services {
    position: absolute;
    left: 30px;
    top: 385px;
    list-style: none;
    font-family: "Gochi Hand", cursive;
    font-size: 50px;
    line-height: 54px;
    color: var(--chalk);
  }
  .services li::before {
    content: "";
    display: inline-block;
    width: 13px;
    height: 13px;
    margin-right: 6px;
    border: 3px solid var(--chalk);
    border-radius: 50%;
    vertical-align: middle;
  }
  .services li:nth-child(2) { margin-left: -4px; }
  .services li:nth-child(3) { margin-left: 6px; }
  .services li:nth-child(4) { margin-left: 8px; }
  .studio-name {
    position: absolute;
    left: 590px;
    top: 290px;
    width: 520px;
    text-align: center;
    font-family: "Anton", sans-serif;
    font-size: 108px;
    line-height: 1;
    color: var(--brand-pink);
    letter-spacing: 3px;
  }
  .studio-name .studio-sub {
    display: block;
    margin-top: 22px;
    font-size: 58px;
    letter-spacing: 10px;
    color: var(--brand-pink);
  }
  .on-label {
    position: absolute;
    left: 392px;
    top: 680px;
    font-family: "Gochi Hand", cursive;
    font-size: 62px;
    color: var(--chalk);
    line-height: 1;
  }
  .platform {
    position: absolute;
    left: 443px;
    top: 775px;
    width: 738px;
    height: 93px;
    display: flex;
    align-items: center;
    justify-content: center;
    gap: 18px;
  }
  .platform-mark {
    width: 46px;
    height: 46px;
    border-radius: 50%;
    background: var(--harbor-blue);
  }
  .platform-name {
    font-family: "Anton", sans-serif;
    font-size: 64px;
    line-height: 1;
    color: var(--harbor-blue);
  }
</style>
</head>
<body>
<main class="canvas">
  <svg class="artwork" width="1200" height="901" viewBox="0 0 1200 901" aria-hidden="true">
    <defs>
      <clipPath id="panel-clip">
        <path d="M540 178 L1160 192 L1150 688 L700 700 Q610 705 575 640 L522 190 Z"/>
      </clipPath>
    </defs>

    <!-- cracks -->
    <g class="cracks" fill="none" stroke="var(--crack)" stroke-width="2" opacity="0.7">
      <path d="M0 160 Q80 150 150 190 T240 260 Q260 320 245 360"/>
      <path d="M150 190 Q170 140 215 120"/>
      <path d="M245 360 Q300 330 370 300 T470 270"/>
      <path d="M0 590 Q60 610 110 700 T180 900"/>
      <path d="M240 260 Q300 250 330 215"/>
    </g>

    <!-- headline underline sketch -->
    <g class="sketch-lines" stroke="var(--chalk)" stroke-width="2" fill="none" opacity="0.85">
      <path d="M410 138 L780 132"/>
      <path d="M416 146 L770 141"/>
      <path d="M400 160 Q440 170 470 205"/>
      <path d="M410 150 Q450 180 460 215"/>
    </g>

    <!-- paper sheet -->
    <path class="paper-sheet" d="M528 168 L1180 180 L1180 760 L570 770 L528 168 Z" fill="var(--paper-white)"/>

    <!-- black panel -->
    <path class="panel" d="M540 178 L1160 192 L1150 688 L700 700 Q610 705 575 640 L522 190 Z" fill="var(--panel-black)"/>
    <g class="panel-stripes" clip-path="url(#panel-clip)" fill="var(--stripe-grey)">
      <rect x="500" y="230" width="680" height="16"/>
      <rect x="500" y="262" width="680" height="16"/>
      <rect x="500" y="294" width="680" height="16"/>
      <rect x="500" y="326" width="680" height="16"/>
      <rect x="500" y="358" width="680" height="16"/>
      <rect x="500" y="390" width="680" height="16"/>
      <rect x="500" y="422" width="680" height="16"/>
      <rect x="500" y="454" width="680" height="16"/>
    </g>
    <!-- curled corner -->
    <path class="panel-curl" d="M575 640 Q610 705 700 700 Q640 740 600 730 Q570 700 575 640 Z" fill="#2a2a2a"/>

    <!-- bottom frame lines -->
    <g class="frame-lines" stroke="var(--chalk)" stroke-width="2" fill="none">
      <path d="M395 760 L1181 760"/>
      <rect x="443" y="775" width="738" height="93"/>
    </g>

    <!-- tick -->
    <path class="tick" d="M480 730 Q500 745 515 760 Q560 690 640 650" stroke="var(--chalk)" stroke-width="5" fill="none" stroke-linecap="round" stroke-linejoin="round"/>
  </svg>

  <h1 class="headline">HIRE ME</h1>

  <ul class="services">
    <li>Design</li>
    <li>Web</li>
    <li>Drawing</li>
    <li>Logo...</li>
  </ul>

  <p class="studio-name">PRISM LANE<span class="studio-sub">MEDIA</span></p>

  <p class="on-label">on</p>

  <div class="platform">
    <span class="platform-mark"></span>
    <span class="platform-name">PixelHarbor</span>
  </div>
</main>
</body>
</html>
```